Flyer for outback tour company

Trifold flyer with a page for each tour that we offer (4 different tours) as well as a front page and a contact page.

Front page: Kestrel Trails logo + an overview of the tours on offer:
- Premium Tour of the Village and Ridgelands
- Wirra Flats Highlights Tour
- Dusk Ridgelands Tour
- Subterranean Gemhunt (prospecting) Tour.

Page 2-5: description of each tour with pricing/duration.

Last page (back of brochure): contact details.
Ph: 0487 216 054
E-mail: kestreltrailsaus@mailbox-example.net
Online bookings: www.kestreltrailsaus-example.com.au.
Tours can also be booked directly through the reception at the Corella Bluff Desert Lodge and the Clay Den Inn. Please include the logos for Corella Bluff and Clay Den on the last page.

Target Market(s)

Travellers/tourists

Industry/Entity Type

Tourism/tour company

Font styles to use
Sans Serif

Requirements
Must have
• In regards to the pictures… the picture with the tour guide shining the torch should be on the page with the Gemhunt Tour. The other pictures of the cave tunnels should only be on the premium tour/Gemhunt Tour or front/back page.

```html
<!DOCTYPE html>
<html lang="en">
<head>
<meta charset="utf-8">
<title>Kestrel Trails – Trifold Flyer</title>
<link href="https://fonts.googleapis.com/css2?family=Montserrat:wght@400;500;600;700&display=swap" rel="stylesheet">
<style>
:root{
  --backdrop:#2fa5cc;
  --dark:#33221a;
  --dark-deep:#2a1b14;
  --rust:#7b4a22;
  --ochre:#a66d2b;
  --orange:#eb9a2e;
  --slate:#4f7690;
  --white:#ffffff;
  --text-light:#f3ece4;
  --rust-text:#a4541c;
}
*{box-sizing:border-box;margin:0;padding:0}
html,body{width:1200px;height:813px;overflow:hidden}
body{background:var(--backdrop);font-family:"Montserrat",Arial,sans-serif;position:relative;color:var(--text-light)}
.spread{position:absolute;top:174px;width:476px;height:368px;overflow:hidden}
.spread--outside{left:81px}
.spread--inside{left:642px}
.panel{position:absolute;top:0;height:368px;overflow:hidden}
.small{font-size:7px;line-height:10px}
.label{color:var(--orange);font-weight:600}
.strong{font-weight:700}
.rule{border:0;border-top:1.2px dashed var(--white);margin:4px 0 6px;position:relative;height:0}
.rule::before,.rule::after{content:"";position:absolute;top:-2.5px;width:4px;height:4px;border-radius:50%;background:var(--white)}
.rule::before{left:-1px}.rule::after{right:-1px}
.rule--orange{border-top-color:var(--orange)}
.rule--orange::before,.rule--orange::after{background:var(--orange)}
.ticks{list-style:none}
.ticks li{position:relative;padding-left:11px;margin-bottom:7px}
.ticks li::before{content:"";position:absolute;left:1px;top:1.5px;border-left:6px solid var(--orange);border-top:3.5px solid transparent;border-bottom:3.5px solid transparent}

/* outside spread */
.premium{left:0;width:157px;background:linear-gradient(180deg,#3d271c,#2f1f17 60%,#3a2519);padding:19px 14px 0 17px}
.premium p{margin-bottom:10px}
.contact{left:157px;width:160px}
.contact svg{position:absolute;inset:0}
.contact__inner{position:absolute;inset:0}
.contact__title{position:absolute;left:20px;top:14px;font-size:11.5px;font-weight:600;color:var(--orange)}
.contact__rule{position:absolute;left:12px;right:10px;top:33px}
.contact__phone{position:absolute;left:36px;top:40px;font-size:11.5px;font-weight:700;line-height:17px}
.contact__body{position:absolute;left:12px;top:114px;width:140px;color:var(--rust-text)}
.contact__body p{margin-bottom:10px}
.contact__body .label{color:var(--orange)}
.partners{position:absolute;left:12px;top:232px;width:140px;display:flex;align-items:center;gap:6px}
.partner-lodge{font-size:6px;font-weight:700;color:var(--rust)}
.divider{width:1px;height:26px;background:var(--rust)}
.badge{width:30px;height:16px;border-radius:3px;background:#2b5a9c}
.badge--green{background:#8cbf3f;border-radius:50%;width:18px;height:18px}
.clayden{position:absolute;left:48px;top:278px;display:flex;align-items:center;gap:3px;font-size:10px;font-weight:600;color:var(--rust-text)}
.clayden i{display:block;width:12px;height:12px;background:#c9601f}
.front{left:317px;width:159px;background:var(--rust)}
.front svg{position:absolute;inset:0}
.brand{position:absolute;left:0;right:0;top:26px;display:flex;flex-direction:column;align-items:center;gap:5px}
.brand i{display:block;width:14px;height:14px;background:#a6541d}
.brand span{font-size:13px;font-weight:700;color:#2a1b14;letter-spacing:.2px}
.tour-index{position:absolute;left:13px;top:106px;width:140px;list-style:none}
.tour-index li{position:relative;padding-left:10px;font-size:9px;line-height:14.5px;font-weight:700;text-transform:uppercase;color:var(--white)}
.tour-index li::before{content:"";position:absolute;left:0;top:3px;border-left:6px solid var(--orange);border-top:3.5px solid transparent;border-bottom:3.5px solid transparent}
.tour-index li.alt{color:var(--orange)}
.tour-index .rule{margin:3px 0 6px 10px}

/* inside spread */
.tour{width:159px}
.tour:nth-child(1){left:0;background:var(--dark)}
.tour:nth-child(2){left:159px;background:var(--ochre)}
.tour:nth-child(3){left:317px;background:var(--dark)}
.photo{position:absolute;left:0;right:0}
.photo--top{top:0;height:58px}
.photo--bottom{top:301px;height:67px}
.tour__body{position:absolute;top:58px;left:0;right:0;height:243px}
.tour__text{position:absolute;font-size:7px;line-height:10px}
.tour__text p{margin-bottom:10px}
.frame{position:absolute;border:1.2px dashed var(--orange)}
</style>
</head>
<body>

<!-- Outside spread -->
<section class="spread spread--outside">
  <article class="panel premium small">
    <div class="label">Premium Tour of the Village and the Ridgelands:</div>
    <hr class="rule">
    <p><span class="label">$99 adults/$75</span> children<br><span class="label">Duration:</span> approx. 5 hours<br><span class="label">1pm</span> start</p>
    <p>This tour is designed for those who want a more personal, authentic experience. Smaller groups, bigger experience. Sit back and relax in our spacious air-conditioned 4wd vehicle as we take you places in and around Wirra Flats that the others can't.</p>
    <div class="label">The tour includes:</div>
    <hr class="rule">
    <ul class="ticks">
      <li>The Old Stone Underground Church.</li>
      <li>Modern Underground Home (dugout).</li>
      <li>The Moon Plains</li>
      <li>The Dingo Fence</li>
      <li>The Ridgelands.</li>
      <li>Underground Mine Tour at our private claim in the opal fields (exclusive to Kestrel Trails)</li>
    </ul>
  </article>

  <article class="panel contact">
    <svg width="160" height="368" viewBox="0 0 160 368" aria-hidden="true">
      <rect width="160" height="368" fill="#33221a"/>
      <path d="M0 0H160V88C120 72 80 70 40 92 25 100 12 104 0 104Z" fill="#4f7690"/>
      <path d="M0 104C12 104 25 100 40 92 80 70 120 72 160 88V368H0Z" fill="#33221a" opacity="0"/>
      <path d="M0 106C20 106 35 96 55 86 90 70 130 74 160 90V318C140 330 120 336 100 334 60 330 30 320 0 296Z" fill="#ffffff"/>
    </svg>
    <div class="contact__inner">
      <div class="contact__title">CONTACT DETAILS:</div>
      <hr class="rule contact__rule">
      <div class="contact__phone"><span style="color:var(--orange)">Phone:</span><br>0487 216 054</div>
      <div class="contact__body small">
        <p><span class="label">E-mail:</span><br>kestreltrailsaus@mailbox-example.net</p>
        <p><span class="label">Online bookings:</span><br>www.kestreltrailsaus-example.com.au</p>
        <p>Tours can also be booked directly through the reception at the Corella Bluff Desert Lodge and the Clay Den Inn.</p>
      </div>
      <div class="partners">
        <span class="partner-lodge">Corella Bluff</span>
        <span class="divider"></span>
        <span class="badge" role="img" aria-label="Partner holiday park badge"></span>
        <span class="divider"></span>
        <span class="badge badge--green" role="img" aria-label="Partner village badge"></span>
      </div>
      <div class="clayden"><i></i>Clay Den</div>
    </div>
  </article>

  <article class="panel front">
    <svg width="159" height="368" viewBox="0 0 159 368">
      <path d="M0 0H159V60C140 90 110 98 80 96 45 94 20 98 0 110Z" fill="#ffffff"/>
      <defs><linearGradient id="outbackView" x1="0" y1="0" x2="0" y2="1">
        <stop offset="0" stop-color="#1f5ea8"/><stop offset=".45" stop-color="#6f9bc8"/>
        <stop offset=".6" stop-color="#b7773a"/><stop offset="1" stop-color="#6e3a1a"/>
      </linearGradient></defs>
      <path d="M0 320C25 280 60 265 100 268 125 270 145 275 159 282V368H0Z" fill="url(#outbackView)" role="img" aria-label="Photo of desert ridgelands under a blue sky"/>
    </svg>
    <div class="brand"><i></i><span>KESTREL TRAILS</span></div>
    <ul class="tour-index">
      <li>Premium Tour of the Village and Ridgelands</li>
      <hr class="rule">
      <li class="alt">Wirra Flats Highlights Tour</li>
      <hr class="rule">
      <li>Dusk Ridgelands Tour</li>
      <hr class="rule">
      <li class="alt">Subterranean Gemhunt (Prospecting) Tour.</li>
    </ul>
  </article>
</section>

<!-- Inside spread -->
<section class="spread spread--inside">
  <article class="panel tour">
    <div class="photo photo--top" role="img" aria-label="Silhouette of a mining rig against a sunset sky" style="background:linear-gradient(180deg,#3a4a7a,#c46a3a 65%,#1c1410)"></div>
    <div class="tour__body">
      <div class="frame" style="left:13px;top:15px;width:133px;height:211px;border-right:0"></div>
      <div class="tour__text" style="left:22px;top:30px;width:125px">
        <p><span class="label">Wirra Flats Highlights Tour:</span><br><span class="strong">$85</span></p>
        <p><span class="label">adults/ $59</span> children Family rate (2 adults and 2 children): <span class="label">$270</span></p>
        <p><span class="label">Duration approx:</span> <span class="strong">5 hours</span></p>
        <p>A tour that gives you a great insight and introduction into this unique outback town and the surrounding area. Highlights include: - Yarrin Opal Mine &amp; Museum - The Old Stone Underground Church. -The dingo fence - The Moon Plains - The Ridgelands</p>
      </div>
    </div>
    <div class="photo photo--bottom" role="img" aria-label="Photo of a tour truck parked below a desert mesa" style="background:linear-gradient(180deg,#8a6a5a,#b07a50 55%,#6d4a30)"></div>
  </article>

  <article class="panel tour">
    <div class="photo photo--top" role="img" aria-label="Photo of an underground mine tunnel" style="background:linear-gradient(90deg,#7c7a74,#b9b5ac 50%,#4a3c30)"></div>
    <div class="tour__body">
      <div class="frame" style="left:-1px;top:30px;width:120px;height:196px;border-left:0;border-top:0"></div>
      <div class="tour__text" style="left:12px;top:12px;width:140px;color:var(--white)">
        <p><span class="label">Dusk Ridgelands Tour:</span> <span class="strong">$60</span></p>
        <p><span class="label">Duration approx.</span> 3.5 hours</p>
        <p><span class="label">Departs 3 hours</span> before sunset<br>A perfect way to end the day. Take in the spectacular views of the colourful Ridgelands. Watch the sun go down across the desert horizon, while enjoying a hot beverage (tea, coffee, hot chocolate) in one hand and a home-made scone in the other.</p>
        <p><span class="label">This tour includes:</span></p>
        <ul class="ticks" style="margin-top:2px">
          <li style="margin-bottom:10px">The Dingo fence</li>
          <li style="margin-bottom:10px">The Moon Plains</li>
          <li>The Ridgelands</li>
        </ul>
      </div>
    </div>
    <div class="photo photo--bottom" role="img" aria-label="Photo of a striped ochre desert ridge" style="background:linear-gradient(180deg,#2f6ab0,#c58a4a 40%,#9a5a2a)"></div>
  </article>

  <article class="panel tour">
    <div class="photo photo--top" role="img" aria-label="Photo of two glasses on red desert ground at dusk" style="background:linear-gradient(180deg,#6a5a4a,#4a3424 60%,#2a1a12)"></div>
    <div class="tour__body">
      <div class="frame" style="left:0;top:12px;width:147px;height:223px;border-left:0;border-top:0;border-bottom:0"></div>
      <div class="tour__text" style="left:18px;top:12px;width:125px">
        <p><span class="label">Subterranean Gemhunt (prospecting) Tour:</span> <span class="strong">$50</span></p>
        <p><span class="label">Duration approx.</span> 2 hours</p>
        <p><span class="label">9.30am</span> start</p>
        <p>This tour is ideal for those who don't mind getting down and dirty whilst searching for their own opals.<br>Exclusive to Kestrel Trails, this impressive opal mine has extracted hundreds of thousands of dollars worth of opal.<br>After a quick introduction to prospecting, you will be handed a blacklight, sieve and shovel to explore the tailings in the hopes of finding your own piece of opal to take home with you. A truly unique experience.</p>
      </div>
    </div>
    <div class="photo photo--bottom" role="img" aria-label="Photo of white chalk hills under a cloudy blue sky" style="background:linear-gradient(180deg,#4f7fc0,#9fb8d8 40%,#e8e4dc 65%,#b89a70)"></div>
  </article>
</section>

</body>
</html>
```